I need a website built for my organization.
We are the world's largest network of music producers.
The website should be professional, sharp, and high quality., We need a website built for The Halvern Sound Guild. We are one of the World's largest association of music producers.
The site must be professional, sharp, and high quality., I need a website built for my organization.
The site must be professional, sharp, and high quality.
Somewhere in the top half of the site there should be a form for the user to fill out. The details of the form are as follows:
Title (large and bold): Contact Us or Submit Your Music
Fields to include (* = required): First Name*, Last Name*, Age, Zip Code, Email Address*, Daytime Phone, Evening Phone, Comments
Then, there will be a "submit" button to proceed to next step of form. Just below the "submit" button, should be the following verbiage: "After submitting, you will have the opportunity to upload demos of your music (optional) and provide other pertinent information about yourself, band, or group."
Target Market(s)
Music producers and aspiring musicians
Industry/Entity Type
Group
Colors
Designer to choose colors to be used in the design.
Look and feel

```html
<!DOCTYPE html>
<html lang="en">
<head>
<meta charset="utf-8">
<title>The Halvern Sound Guild</title>
<link href="https://fonts.googleapis.com/css2?family=Rokkitt:wght@400;500&family=Open+Sans:ital,wght@0,400;0,700;1,400&family=Bitter:ital,wght@1,800&family=Questrial&display=swap" rel="stylesheet">
<style>
  :root {
    --ink: #000000;
    --gold: #f4a93a;
    --tab-gold: #eea232;
    --button-gold: #fbb64c;
    --panel: rgba(150, 150, 150, 0.88);
    --field: #ebebeb;
    --field-text: #7a7a7a;
    --white: #ffffff;
    --tab-text: #1a1a1a;
    --band: rgba(0, 0, 0, 0.42);
  }
  * { box-sizing: border-box; margin: 0; padding: 0; }
  html, body { width: 1200px; height: 690px; overflow: hidden; background: var(--ink); }
  .page { position: relative; width: 1200px; height: 690px; overflow: hidden; background: var(--ink); }

  .hero-photo {
    position: absolute; left: 110px; top: 90px; width: 1090px; height: 600px;
    background:
      radial-gradient(ellipse 230px 300px at 870px 300px, rgba(190,170,130,0.55), rgba(0,0,0,0) 70%),
      radial-gradient(ellipse 300px 330px at 450px 260px, rgba(150,120,80,0.75), rgba(40,30,20,0.3) 65%, rgba(0,0,0,0) 85%);
  }

  .brand {
    position: absolute; left: 55px; top: 30px;
    font-family: "Rokkitt", serif; font-weight: 500; font-size: 34px;
    color: var(--gold); letter-spacing: 0.5px;
  }

  .main-nav { position: absolute; left: 708px; top: 38px; display: flex; align-items: center; }
  .main-nav a {
    font-family: "Rokkitt", serif; font-weight: 400; font-size: 16px;
    color: var(--white); text-decoration: none; letter-spacing: 0.6px;
    position: absolute; top: 8px; white-space: nowrap;
  }
  .nav-home { position: absolute; left: 0; top: 0; }

  .headline-band {
    position: absolute; left: 454px; top: 503px; width: 726px; height: 123px;
    background: var(--band);
  }
  .headline {
    position: absolute; left: 444px; top: 502px; width: 746px;
    font-family: "Questrial", sans-serif; font-weight: 400; font-size: 43px; line-height: 57px;
    color: var(--white); text-align: center; white-space: nowrap;
  }

  .contact-tab {
    position: absolute; left: 0; top: 258px; width: 62px; height: 213px;
    background: var(--tab-gold); border-radius: 0 4px 4px 0;
  }
  .contact-tab span {
    position: absolute; left: 31px; top: 106px;
    transform: translate(-50%, -50%) rotate(-90deg);
    font-family: "Open Sans", sans-serif; font-weight: 700; font-size: 24px;
    color: var(--tab-text); white-space: nowrap; letter-spacing: 0.5px;
  }

  .submit-form {
    position: absolute; left: 62px; top: 132px; width: 372px; height: 489px;
    background: var(--panel);
  }
  .field {
    position: absolute; height: 34px; background: var(--field);
    font-family: "Open Sans", sans-serif; font-style: italic; font-size: 13px;
    color: var(--field-text); padding-left: 16px; line-height: 34px; text-transform: uppercase;
  }
  .field-half { width: 155px; }
  .field-full { width: 323px; }
  .field-age { width: 105px; }
  .field-message { height: 51px; line-height: 56px; }
  .age-caret { position: absolute; right: 12px; top: 13px; }
  .field-cue { position: absolute; left: 16px; top: 218px; }

  .send-button {
    position: absolute; left: 24px; top: 356px; width: 323px; height: 39px;
    background: var(--button-gold); border: none;
    font-family: "Bitter", serif; font-style: italic; font-weight: 800; font-size: 21px;
    color: var(--white); text-transform: uppercase; letter-spacing: 0.3px;
  }
  .form-note {
    position: absolute; left: 28px; top: 408px; width: 330px;
    font-family: "Open Sans", sans-serif; font-size: 12px; line-height: 16px; color: var(--white);
  }
</style>
</head>
<body>
<div class="page">
  <div class="hero-photo" role="img" aria-label="Sepia photograph of a long-haired musician beside a studio condenser microphone"></div>

  <div class="brand">Halvern Sound Guild</div>

  <nav class="main-nav">
    <svg class="nav-home" width="32" height="30" viewBox="0 0 32 30" aria-label="Home">
      <path d="M16 2 L1 15 L5 15 L5 28 L13 28 L13 20 L19 20 L19 28 L27 28 L27 15 L31 15 Z" fill="#ffffff"/>
      <rect x="22" y="4" width="4" height="7" fill="#ffffff"/>
    </svg>
    <a href="#" style="left:63px">NEWS</a>
    <a href="#" style="left:133px">AUDIO</a>
    <a href="#" style="left:207px">VIDEOS</a>
    <a href="#" style="left:287px">GALLERY</a>
    <a href="#" style="left:381px">CONTACT</a>
  </nav>

  <div class="headline-band"></div>
  <h1 class="headline">World's largest network of Music<br>Producers</h1>

  <div class="contact-tab"><span>CONTACT US</span></div>

  <form class="submit-form">
    <div class="field field-half" style="left:24px;top:37px">First name</div>
    <div class="field field-half" style="left:190px;top:37px">Last name</div>
    <div class="field field-half" style="left:24px;top:95px">Daytime phone</div>
    <div class="field field-half" style="left:190px;top:95px">Evening phone</div>
    <div class="field field-full" style="left:24px;top:154px">Email</div>
    <div class="field field-half" style="left:24px;top:215px">Zip code</div>
    <div class="field field-age" style="left:190px;top:215px">Age
      <svg class="age-caret" width="18" height="10" viewBox="0 0 18 10"><path d="M0 0 H18 L9 10 Z" fill="#333333"/></svg>
    </div>
    <svg class="field-cue" width="22" height="30" viewBox="0 0 22 30">
      <path d="M2 2 L12 15 L2 28 M9 2 L19 15 L9 28" fill="none" stroke="#ffffff" stroke-width="2"/>
    </svg>
    <div class="field field-full field-message" style="left:24px;top:276px">Message</div>
    <button class="send-button" type="submit">Send your message</button>
    <p class="form-note">After submitting, you will have the opportunity to upload demos of your music (optional) and provide other pertinent information about yourself, band, or group.</p>
  </form>
</div>
</body>
</html>
```